Automotive Mechanic Website Design

We are working with an auto repair shop in California.
A few websites for inspiration:
https://brindlecovemotors.example
https://www.folionest.example/gallery/57316284/Torvane-Auto-Services-Repair-SiteKit-Theme
http://www.quelbrightmotors.example
https://www.halvikgarage.example
https://www.pdmotorhaus.example
Thank you for taking the time to consider designing a website for us. We are web developers based in Stockton, CA, USA. Most of our projects go through the same process. Understanding this process may help you win a project with us. We custom-code all of our websites in-house. We don’t have any requirements as to what tools you use for your design, but we ask that you follow these guidelines.
IMAGES:
If you use any images or icons in the design, we ask that you have a link to the asset so we can purchase the image/icon. Most of the designs we submit do not have the customer’s images on them unless they have some great images. Be creative; show us the feeling you are trying to portray with your image choices. Use any royalty-free site you choose. We subscribe to Adobe and mainly use their images, but we can purchase images outside of Adobe. PLEASE NOTE: we will not submit designs to clients with watermarks on the images.
FONTS:
We ask that you identify the fonts you’re using in the design. This can be done in a message if you want. We typically use Google Fonts and Adobe Fonts.
CONTENT:
We're always open to different content and ideas. We often submit designs with stock images so the client can see our vision. We typically take pictures after the website launch to use their images with our vision. Lorem Ipsum is fine for paragraphs, but we ask that you make the Headers with correct English. We want to be able to show the vision and identify the sections of the website.
INSPIRATION:
We typically add a couple of links in the brief of websites we like to help you get started in your design.
REVISIONS:
We do not often ask for revisions of the designs unless we see something in the design that may not appeal to the client. If there are slight changes that we want to make, we do that in the development process.
FEEDBACK:
We rarely give feedback on designs during the design process. We are working on many website projects and do not have the time to provide feedback. We usually respond if your request is well thought out and asks specific questions, but a note asking “feedback, please” usually goes unanswered.

```html
<!DOCTYPE html>
<html lang="en">
<head>
<meta charset="utf-8">
<title>Korvex Auto Repair</title>
<link rel="stylesheet" href="https://fonts.googleapis.com/css2?family=Teko:wght@400;500;600&family=Open+Sans:wght@400;600&family=Lora:ital@1&display=swap">
<style>
:root{
  --red:#f44646;
  --red-dark:#d93434;
  --dark:#16181e;
  --ink:#1d1d1f;
  --muted:#555;
  --light:#f3f3f4;
  --white:#fff;
  --line:#cfcfcf;
}
*{box-sizing:border-box;margin:0;padding:0}
html,body{width:1200px;height:4612px;overflow:hidden}
body{position:relative;background:var(--white);color:var(--ink);font-family:"Open Sans",sans-serif;font-size:11px}
.abs{position:absolute}
.display{font-family:"Teko",sans-serif;font-weight:500;text-transform:uppercase;line-height:.95;letter-spacing:.5px}
.eyebrow{font-size:10px;font-weight:600;color:var(--red);text-transform:uppercase;letter-spacing:.3px}
.eyebrow::after{content:"";display:block;width:62px;height:1px;background:var(--red);margin-top:7px}
.para{font-size:10.5px;line-height:19px;color:#333}
.btn-outline{display:flex;align-items:center;justify-content:center;border:2px solid var(--red);color:var(--red);font-family:"Teko",sans-serif;font-size:12px;font-weight:500;letter-spacing:.6px;text-transform:uppercase;background:transparent}
.btn-light{border-color:#fff;color:#fff}
.btn-solid{display:flex;align-items:center;justify-content:center;background:var(--red);color:#fff;font-family:"Teko",sans-serif;font-size:12px;font-weight:500;letter-spacing:.6px;text-transform:uppercase}
.photo{position:absolute}

/* top bar */
.topbar{top:0;left:0;width:1200px;height:40px;background:#fff}
.topbar-rating{left:0;top:0;width:330px;height:40px;background:var(--dark);clip-path:polygon(0 0,100% 0,94% 100%,0 100%);color:#fff;font-size:11px;display:flex;align-items:center;padding-left:73px;gap:6px}
.topbar-rating .stars{color:var(--red);letter-spacing:1px}
.topbar-location{left:650px;top:0;height:40px;display:flex;align-items:center;gap:6px;font-size:11px;color:#333}
.topbar-cta{left:962px;top:0;width:163px;height:36px;font-size:12px}

/* nav */
.nav{top:40px;left:0;width:1200px;height:53px;border-top:1px solid #eee;background:#fff}
.brand{font-family:"Teko",sans-serif;font-weight:600;color:var(--red);text-transform:uppercase;line-height:1}
.nav .brand{left:75px;top:6px;font-size:22px;line-height:20px}
.nav-links{left:378px;top:0;height:53px;display:flex;align-items:center;gap:33px;list-style:none}
.nav-links li{font-family:"Teko",sans-serif;font-size:12px;font-weight:500;letter-spacing:.4px;text-transform:uppercase;color:#222;white-space:nowrap}
.nav-links li.active{color:var(--red)}
.nav-phone{left:1018px;top:0;height:53px;display:flex;align-items:center;gap:8px;font-family:"Teko",sans-serif;font-size:17px;font-weight:500}

/* hero */
.hero{top:93px;left:0;width:1200px;height:532px;background:linear-gradient(100deg,#2c2f35 0%,#3c4046 40%,#1d2026 70%,#4a4e55 100%)}
.hero-title{left:200px;top:110px;font-size:86px;line-height:88px;color:#fff}
.hero-cta{left:200px;top:381px;width:162px;height:36px}
.hero-dots{left:982px;top:214px;display:flex;flex-direction:column;gap:16px}
.hero-dots span{width:14px;height:14px;border:2px solid #fff;border-radius:50%}
.hero-dots span.on{background:#fff}

/* about */
.about{top:625px;left:0;width:1200px;height:802px;background:linear-gradient(180deg,#ffffff 0%,#f1f2f4 55%,#e6e8ea 100%)}
.about-photo{left:75px;top:93px;width:425px;height:450px;background:linear-gradient(135deg,#6f747a,#3a3e44 60%,#9a9ea3)}
.experience{left:381px;top:344px;width:206px;height:229px;background:var(--red);color:#fff}
.experience .frame-tl{position:absolute;left:24px;top:24px;width:60px;height:40px;border-left:2px solid #fff;border-top:2px solid #fff}
.experience .frame-br{position:absolute;right:14px;bottom:16px;width:60px;height:50px;border-right:2px solid #fff;border-bottom:2px solid #fff}
.experience p{position:absolute;left:28px;top:50px;font-family:"Teko",sans-serif;font-size:27px;line-height:30px}
.experience p .big{font-size:62px;vertical-align:-8px}
.about-copy{left:612px;top:172px;width:385px}
.about-copy h2{font-size:40px;margin:20px 0 10px}
.about-copy .para+.para{margin-top:18px}
.about-copy .btn-outline{width:124px;height:36px;margin-top:22px}
.stats{left:200px;top:646px;display:flex;gap:0}
.stat{width:206px;display:flex;align-items:center;gap:10px}
.stat-num{height:84px;padding:0 6px 0 14px;border-left:2px solid #333;border-top:2px solid #333;border-bottom:2px solid #333;font-family:"Teko",sans-serif;font-size:60px;font-weight:500;color:var(--red);line-height:92px}
.stat-label{font-size:12px;line-height:15px;color:#222}

/* diagnostic band */
.diagnostic{top:1427px;left:200px;width:1000px;height:187px;background:linear-gradient(90deg,#15171c 0%,#1c1f25 45%,#3d4147 75%,#2b2e33 100%);clip-path:polygon(63px 0,100% 0,100% 100%,0 100%)}
.diagnostic .eyebrow{position:absolute;left:95px;top:34px}
.diagnostic h2{position:absolute;left:95px;top:70px;font-size:40px;color:#fff;line-height:44px}
.diagnostic .btn-outline{position:absolute;left:636px;top:77px;width:162px;height:33px}

/* services */
.services-head{left:75px;top:1705px}
.services-head h2{font-size:40px;line-height:44px;margin-top:14px}
.services-cta{left:962px;top:1787px;width:163px;height:36px}
.service-grid{left:75px;top:1886px;display:flex;gap:25px}
.service-card{position:relative;width:244px;height:356px;background:#fff;box-shadow:0 4px 18px rgba(0,0,0,.08)}
.service-card .photo{left:0;top:0;width:244px;height:290px}
.service-card svg{position:absolute;left:0;top:228px}
.service-card h3{position:absolute;left:32px;top:290px;font-family:"Teko",sans-serif;font-weight:500;font-size:16px;line-height:20px;text-transform:uppercase;color:#222}

/* call */
.call{top:2242px;left:0;width:1200px;height:224px;background:linear-gradient(180deg,#fff 0%,#eeeff1 100%)}
.call h3{position:absolute;top:42px;width:1200px;text-align:center;font-size:31px;color:#222}
.call .phone{position:absolute;top:92px;width:1200px;display:flex;justify-content:center;align-items:center;gap:10px;font-family:"Teko",sans-serif;font-size:42px;font-weight:500;color:var(--red)}

/* vehicles */
.vehicles{top:2466px;left:0;width:587px;height:466px;background:var(--red)}
.car{position:absolute;width:96px;text-align:center;color:#fff;font-family:"Teko",sans-serif;font-size:15px;font-weight:500;text-transform:uppercase}
.car .shape{display:block;width:92px;height:36px;margin:0 auto 10px;border-radius:40% 48% 12% 12%/70% 70% 20% 20%}
.car .shape.dark{background:linear-gradient(180deg,#2a2c31,#0f1013)}
.car .shape.blue{background:linear-gradient(180deg,#6a7a92,#3c4758)}
.car .shape.white{background:linear-gradient(180deg,#f4f4f4,#c8c8c8)}
.car .shape.redc{background:linear-gradient(180deg,#c51f22,#7e0e10)}
.car .shape.silver{background:linear-gradient(180deg,#d8d9dc,#9fa2a7)}
.vehicles-copy{left:612px;top:2629px;width:400px}
.vehicles-copy h2{font-size:40px;line-height:44px}
.vehicles-copy .para{margin-top:16px}
.vehicles-copy .btn-outline{width:162px;height:36px;margin-top:18px}

/* testimonials */
.testimonials{top:2932px;left:0;width:1200px;height:593px;background:linear-gradient(90deg,#fff 0%,#fff 40%,#e9eaec 58%,#cfd1d4 80%,#e4e5e7 100%)}
.testimonial-photo{left:560px;top:0;width:640px;height:593px;background:linear-gradient(90deg,rgba(255,255,255,0) 0%,rgba(190,192,196,.55) 40%,rgba(160,162,166,.5) 70%,rgba(230,230,232,.3) 100%)}
.testimonial-copy{left:200px;top:100px;width:370px}
.testimonial-copy h2{font-size:40px;margin-top:14px}
.quote-mark{margin-top:22px;font-family:"Lora",serif;font-size:56px;line-height:40px;color:var(--red)}
.testimonial-copy blockquote{margin-top:14px;font-family:"Lora",serif;font-style:italic;font-size:14px;line-height:22px;color:#333}
.testimonial-copy cite{display:block;margin-top:20px;font-style:normal;font-family:"Teko",sans-serif;font-weight:500;font-size:16px;text-transform:uppercase}
.pager{display:flex;gap:8px;margin-top:24px}
.pager span{width:12px;height:12px;border-radius:50%;border:1.5px solid var(--red)}
.pager span.on{background:var(--red)}
.testimonial-copy .btn-solid{width:124px;height:36px;margin-top:44px}

/* partners */
.partners{top:3525px;left:200px;width:800px;height:72px;display:flex;align-items:center;justify-content:space-between}
.partner{background:#2a2a2c;opacity:.85}

/* directions */
.directions{left:200px;top:3748px;width:388px}
.directions h2{font-size:40px}
.directions .sub{font-size:21px;color:#333;margin-top:4px}
.directions .field{margin-top:32px;border-bottom:1.5px solid #333;height:32px;font-family:"Lora",serif;font-style:italic;font-size:11px;padding:0 0 0 18px;line-height:24px}
.directions .go{width:62px;height:38px;margin-top:16px;background:var(--dark);color:#fff;display:flex;align-items:center;justify-content:center;font-family:"Teko",sans-serif;font-size:12px;font-weight:500}
.vehicle-lineup{left:0;top:3940px;width:1200px;height:269px;background:linear-gradient(180deg,#f4f4f5 0%,#c9ccd1 45%,#5a6068 75%,#2b2e34 100%)}
.appointment{left:612px;top:3680px;width:387px;height:332px;background:linear-gradient(180deg,var(--red) 0%,var(--red) 62%,rgba(244,70,70,0) 100%);color:#fff;padding:68px 0 0 50px}
.appointment h2{font-size:40px;line-height:38px}
.appointment p{font-size:17px;margin-top:12px}
.appointment .cta{width:176px;height:36px;margin-top:28px;background:#fff;color:var(--red);display:flex;align-items:center;justify-content:center;font-family:"Teko",sans-serif;font-size:12px;font-weight:500;letter-spacing:.5px;text-transform:uppercase}

/* footer */
.footer{left:0;top:4209px;width:1200px;height:403px;background:var(--dark);color:#fff}
.footer .brand{position:absolute;left:75px;top:96px;width:250px;font-size:38px;line-height:34px;text-align:right}
.social{position:absolute;left:138px;top:191px;display:flex;gap:0}
.social span{width:32px;height:32px;border:1px solid var(--red);margin-right:7px}
.social span.on{background:var(--red)}
.footer h4{font-family:"Teko",sans-serif;font-weight:500;font-size:15px;letter-spacing:.4px;text-transform:uppercase}
.footer-contact{position:absolute;left:381px;top:100px}
.footer-hours{position:absolute;left:612px;top:100px}
.footer dl{display:grid;margin-top:24px;row-gap:9px;font-family:"Teko",sans-serif;font-size:15px;line-height:16px}
.footer-contact dl{grid-template-columns:68px 150px}
.footer-hours dl{grid-template-columns:68px 110px}
.footer-contact dt{color:var(--red)}
.footer-copy{position:absolute;left:75px;top:324px;font-size:10px}
.footer-copy b{color:var(--red);font-weight:400}
.footer-legal{position:absolute;left:381px;top:324px;font-size:10px}
.map{left:818px;top:4146px;width:382px;height:466px;background:linear-gradient(180deg,#eef0f2,#e2e5e8)}
.map svg{position:absolute;left:176px;top:238px}
</style>
</head>
<body>

<div class="abs topbar">
  <div class="abs topbar-rating">Korvex Auto Repair <span class="stars">★★★★</span> 723 Reviews</div>
  <div class="abs topbar-location">
    <svg width="10" height="13" viewBox="0 0 10 13"><path d="M5 0a5 5 0 0 0-5 5c0 3.5 5 8 5 8s5-4.5 5-8a5 5 0 0 0-5-5zm0 7a2 2 0 1 1 0-4 2 2 0 0 1 0 4z" fill="var(--red)"/></svg>
    Lorem ipsum work, design - location dammy - 12345
  </div>
  <div class="abs topbar-cta btn-solid">Request an appointment</div>
</div>

<header class="abs nav">
  <div class="abs brand">Korvex<br>Auto Repair</div>
  <ul class="abs nav-links">
    <li class="active">Home</li><li>Services</li><li>Vehicles</li><li>Specials</li><li>Appointments</li><li>About us</li><li>Reviews</li><li>Directions</li>
  </ul>
  <div class="abs nav-phone">
    <svg width="14" height="14" viewBox="0 0 24 24"><path d="M6.6 10.8a15.1 15.1 0 0 0 6.6 6.6l2.2-2.2a1 1 0 0 1 1-.25 11.4 11.4 0 0 0 3.6.57 1 1 0 0 1 1 1V20a1 1 0 0 1-1 1A17 17 0 0 1 3 4a1 1 0 0 1 1-1h3.5a1 1 0 0 1 1 1c0 1.25.2 2.45.57 3.57a1 1 0 0 1-.25 1z" fill="var(--red)"/></svg>
    555-014-2290
  </div>
</header>

<section class="abs hero" role="img" aria-label="Dark sports sedan photographed at dusk beside a misty lake">
  <h1 class="abs display hero-title">Advanced<br>Vehicle Repair<br>Services</h1>
  <div class="abs hero-cta btn-outline btn-light">Contact us today!</div>
  <div class="abs hero-dots"><span></span><span class="on"></span><span></span><span></span></div>
</section>

<section class="abs about">
  <div class="photo about-photo" role="img" aria-label="Mechanics working on a brake disc under a lifted car"></div>
  <div class="abs experience">
    <span class="frame-tl"></span><span class="frame-br"></span>
    <p>More Than<br><span class="big">20</span> Years<br>of Experience</p>
  </div>
  <div class="abs about-copy">
    <div class="eyebrow">Welcome to</div>
    <h2 class="display">Korvex Auto Repair</h2>
    <p class="para">Lorem Ipsum is simply dummy text of the printing and typesetting industry. Lorem Ipsum has been the industry's standard dummy text ever since the 1500s, when an unknown printer took a galley of type and scrambled it to make a type specimen book.</p>
    <p class="para">It has survived not only five centuries, but also the leap into electronic typesetting, remaining essentially unchanged. It was popularised in the 1960s with the release of Pressline sheets containing Lorem Ipsum passages, and more recently with desktop publishing ...</p>
    <div class="btn-outline">Explore more</div>
  </div>
  <div class="abs stats">
    <div class="stat"><div class="stat-num">20</div><div class="stat-label">Years of<br>Experience</div></div>
    <div class="stat"><div class="stat-num">500</div><div class="stat-label">Happy<br>Clients</div></div>
    <div class="stat"><div class="stat-num">980</div><div class="stat-label">Vehicle<br>Repaired</div></div>
    <div class="stat"><div class="stat-num">52</div><div class="stat-label">Awards<br>Winning</div></div>
  </div>
</section>

<section class="abs diagnostic" role="img" aria-label="Workshop interior with a car on the service floor">
  <div class="eyebrow">We offer a</div>
  <h2 class="display">Complete diagnostic for<br>your car</h2>
  <div class="btn-outline btn-light">Contact us today!</div>
</section>

<div class="abs services-head">
  <div class="eyebrow">Our services</div>
  <h2 class="display">Get over 200 car repair services<br>at your home or office</h2>
</div>
<div class="abs services-cta btn-solid">View all services</div>
<div class="abs service-grid">
  <article class="service-card">
    <div class="photo" role="img" aria-label="Hands connecting cables to a car battery" style="background:linear-gradient(135deg,#4a4f57,#23262b)"></div>
    <svg width="244" height="64" viewBox="0 0 244 64"><path d="M0 40 C40 10 80 10 120 30 C160 52 200 44 244 26 V64 H0Z" fill="var(--red)"/><path d="M0 52 C40 22 80 22 120 42 C160 64 200 56 244 38 V64 H0Z" fill="#fff"/></svg>
    <h3>Battery &amp; wheel<br>service</h3>
  </article>
  <article class="service-card">
    <div class="photo" role="img" aria-label="Technician running engine diagnostics on a laptop" style="background:linear-gradient(135deg,#8d949c,#3f444b)"></div>
    <svg width="244" height="64" viewBox="0 0 244 64"><path d="M0 40 C40 10 80 10 120 30 C160 52 200 44 244 26 V64 H0Z" fill="var(--red)"/><path d="M0 52 C40 22 80 22 120 42 C160 64 200 56 244 38 V64 H0Z" fill="#fff"/></svg>
    <h3>Engine<br>diagnostics</h3>
  </article>
  <article class="service-card">
    <div class="photo" role="img" aria-label="Air conditioning pressure gauges attached to an engine" style="background:linear-gradient(135deg,#3a4660,#1c2230)"></div>
    <svg width="244" height="64" viewBox="0 0 244 64"><path d="M0 40 C40 10 80 10 120 30 C160 52 200 44 244 26 V64 H0Z" fill="var(--red)"/><path d="M0 52 C40 22 80 22 120 42 C160 64 200 56 244 38 V64 H0Z" fill="#fff"/></svg>
    <h3>Air conditioning and<br>heating repair</h3>
  </article>
  <article class="service-card">
    <div class="photo" role="img" aria-label="Fresh motor oil being poured into an engine" style="background:linear-gradient(135deg,#6b6f76,#c99a3a 60%,#3a3d42)"></div>
    <svg width="244" height="64" viewBox="0 0 244 64"><path d="M0 40 C40 10 80 10 120 30 C160 52 200 44 244 26 V64 H0Z" fill="var(--red)"/><path d="M0 52 C40 22 80 22 120 42 C160 64 200 56 244 38 V64 H0Z" fill="#fff"/></svg>
    <h3>Oil change and "K"<br>services</h3>
  </article>
</div>

<section class="abs call">
  <h3 class="display">Have any question? Call us today!</h3>
  <div class="phone">
    <svg width="34" height="34" viewBox="0 0 24 24"><path d="M6.6 10.8a15.1 15.1 0 0 0 6.6 6.6l2.2-2.2a1 1 0 0 1 1-.25 11.4 11.4 0 0 0 3.6.57 1 1 0 0 1 1 1V20a1 1 0 0 1-1 1A17 17 0 0 1 3 4a1 1 0 0 1 1-1h3.5a1 1 0 0 1 1 1c0 1.25.2 2.45.57 3.57a1 1 0 0 1-.25 1z" fill="none" stroke="var(--red)" stroke-width="1.6"/><path d="M15 3a6 6 0 0 1 6 6M15 6.5A2.5 2.5 0 0 1 17.5 9" fill="none" stroke="var(--red)" stroke-width="1.6"/></svg>
    (555)-014-2290
  </div>
</section>

<section class="abs vehicles">
  <div class="car" style="left:70px;top:96px"><span class="shape dark" role="img" aria-label="Dark coupe"></span>Brevan</div>
  <div class="car" style="left:240px;top:96px"><span class="shape blue" role="img" aria-label="Blue hatchback"></span>Hyorin</div>
  <div class="car" style="left:405px;top:96px"><span class="shape white" role="img" aria-label="White compact car"></span>Tovara</div>
  <div class="car" style="left:70px;top:210px"><span class="shape redc" role="img" aria-label="Red sedan"></span>Aurex</div>
  <div class="car" style="left:245px;top:210px"><span class="shape white" role="img" aria-label="White crossover"></span>Lyxar</div>
  <div class="car" style="left:408px;top:210px"><span class="shape redc" role="img" aria-label="Red hatchback"></span>Mazeno</div>
  <div class="car" style="left:153px;top:310px"><span class="shape silver" role="img" aria-label="Silver sedan"></span>Mervane</div>
  <div class="car" style="left:325px;top:310px"><span class="shape redc" role="img" aria-label="Red compact car"></span>Mazeno</div>
</section>
<div class="abs vehicles-copy">
  <h2 class="display">Vehicles we<br>service</h2>
  <p class="para">Lorem Ipsum is simply dummy text of the printing and typesetting industry. lorem Ipsum has been the industry's standard dummy text ever unknown.</p>
  <div class="btn-outline">Contact us today!</div>
</div>

<section class="abs testimonials">
  <div class="photo testimonial-photo" role="img" aria-label="Happy couple driving in their car"></div>
  <div class="abs testimonial-copy">
    <div class="eyebrow">Testimonials</div>
    <h2 class="display">Happy clients say</h2>
    <div class="quote-mark">“</div>
    <blockquote>Contrary to popular belief, Lorem Ipsum is not simply random text. It has roots in a piece of classical Latin literature from 45 BC, making it over professor at Ashgrove College in Virginia ...</blockquote>
    <cite>Dana Merrow</cite>
    <div class="pager"><span></span><span class="on"></span><span></span><span></span><span></span></div>
    <div class="btn-solid">View all</div>
  </div>
</section>

<div class="abs partners">
  <span class="partner" role="img" aria-label="Certification badge" style="width:44px;height:44px;border-radius:50%"></span>
  <span class="partner" role="img" aria-label="Parts retailer badge" style="width:84px;height:40px;background:var(--red)"></span>
  <span class="partner" role="img" aria-label="Parts retailer badge" style="width:78px;height:40px;border-radius:6px"></span>
  <span class="partner" role="img" aria-label="Parts supplier badge" style="width:40px;height:40px;border-radius:50%"></span>
  <span class="partner" role="img" aria-label="Parts manufacturer badge" style="width:222px;height:34px"></span>
</div>

<div class="abs directions">
  <h2 class="display">Get directions</h2>
  <p class="sub">Having Trouble Finding Us?</p>
  <div class="field">Enter Starting Address ...</div>
  <div class="go">GO</div>
</div>

<div class="abs vehicle-lineup" role="img" aria-label="Blue sports car, black pickup truck and white sedan lined up on a desert road"></div>

<div class="abs appointment">
  <h2 class="display">Make an online<br>appointment</h2>
  <p>Let Us know how we can help you.</p>
  <div class="cta">Make an appointment now!</div>
</div>

<footer class="abs footer">
  <div class="brand">Korvex<br>Auto Repair</div>
  <div class="social">
    <span role="img" aria-label="Social profile"></span>
    <span class="on" role="img" aria-label="Social profile"></span>
    <span role="img" aria-label="Social profile"></span>
  </div>
  <div class="footer-contact">
    <h4>Contact us</h4>
    <dl>
      <dt>Call Us:</dt><dd>555-014-2290</dd>
      <dt>Email:</dt><dd>info@korvexauto.example</dd>
      <dt>Address:</dt><dd>Lorem House Level 3,<br>1500 Alder Row<br>Lorem</dd>
    </dl>
  </div>
  <div class="footer-hours">
    <h4>Hours of operation</h4>
    <dl>
      <dt>Mon - Fri:</dt><dd>8:00 am - 5:00 pm</dd>
      <dt>Saturday:</dt><dd>By Appointment</dd>
      <dt>Sunday:</dt><dd>Closed</dd>
    </dl>
  </div>
  <p class="footer-copy">© 2023 <b>KORVEX AUTO REPAIR</b>. All Right Reserved</p>
  <p class="footer-legal">Terms and Conditions &nbsp; | &nbsp; Privacy Notice</p>
</footer>

<div class="abs map" role="img" aria-label="Street map showing the shop location">
  <svg width="22" height="30" viewBox="0 0 10 13"><path d="M5 0a5 5 0 0 0-5 5c0 3.5 5 8 5 8s5-4.5 5-8a5 5 0 0 0-5-5zm0 7a2 2 0 1 1 0-4 2 2 0 0 1 0 4z" fill="#e53935"/></svg>
</div>

</body>
</html>
```